Business Card Design

I need a business card for my rental business. The business is named:
Cruise a Trikeway Houston
www.cruiseatrikewayhouston.com
(832) 555-0193
This will be a business card that I will leave at other businesses as advertisement so it needs to have the name, website, and phone number.
Please feel free to be creative. This is a new business so I have no designs.
Thank you very much for your time and I look forward to receiving your designs
Target Market(s)
Local rental customers
Industry/Entity Type
Business
Contact Information for Business Card
Please check out my website:
Font styles to use
Other font styles liked:
- anything creative
Colors
Designer to choose colors to be used in the design.
Requirements
Must have
- Business name, phone, website. Rentals available hourly or daily. Book online

```html
<!DOCTYPE html>
<html lang="en">
<head>
<meta charset="UTF-8">
<title>Cruise a Trikeway Houston — Business Card</title>
<link rel="stylesheet" href="https://fonts.googleapis.com/css2?family=Saira+Condensed:wght@700;800&family=Josefin+Sans:wght@400;600&family=Work+Sans:wght@400;500&display=swap">
<style>
  :root {
    --stage: #161616;
    --card-dark: #232323;
    --card-light: #333333;
    --accent-red: #e8202a;
    --ink-white: #ffffff;
    --emboss-grey: #4b4b4b;
  }
  * { box-sizing: border-box; margin: 0; padding: 0; }
  html, body {
    width: 1200px; height: 900px; overflow: hidden;
    background: var(--stage);
  }
  .canvas {
    width: 1200px; height: 900px;
    display: flex; flex-direction: column;
    align-items: center; justify-content: center; gap: 40px;
  }
  .card {
    position: relative;
    width: 700px; height: 400px;
    background: linear-gradient(135deg, var(--card-dark) 0%, var(--card-light) 100%);
    border-bottom: 10px solid var(--accent-red);
    box-shadow: 0 18px 40px rgba(0,0,0,0.6);
  }
  /* Front */
  .card-front {
    display: flex; align-items: center; justify-content: center;
  }
  .front-name {
    font-family: "Saira Condensed", sans-serif;
    font-weight: 800;
    font-size: 40px;
    letter-spacing: 2px;
    text-transform: uppercase;
    color: var(--emboss-grey);
  }
  /* Back */
  .card-back {
    display: flex; align-items: center;
    padding: 0 40px 0 30px;
  }
  .brand-block {
    width: 320px;
    text-align: center;
    color: var(--ink-white);
    font-family: "Saira Condensed", sans-serif;
    text-transform: uppercase;
  }
  .brand-name {
    font-weight: 800; font-size: 31px; letter-spacing: 1px; line-height: 1.1;
  }
  .brand-tagline {
    font-weight: 700; font-size: 20px; line-height: 1.3; margin-top: 4px;
  }
  .divider {
    width: 3px; height: 130px;
    background: var(--accent-red);
    margin: 0 26px 0 20px;
  }
  .contact-block { color: var(--ink-white); }
  .person-name {
    font-family: "Josefin Sans", sans-serif;
    font-weight: 600; font-size: 34px;
    letter-spacing: 1.5px; text-transform: uppercase;
    color: var(--accent-red); line-height: 1;
  }
  .person-role {
    font-family: "Josefin Sans", sans-serif;
    font-weight: 400; font-size: 20px; letter-spacing: 1px;
    text-transform: uppercase; margin-top: 4px;
  }
  .contact-line {
    font-family: "Work Sans", sans-serif;
    font-size: 19px; letter-spacing: 0.5px; margin-top: 6px;
  }
  .contact-line:first-of-type { margin-top: 26px; }
  .contact-label { color: var(--accent-red); }
</style>
</head>
<body>
<main class="canvas">
  <section class="card card-front" aria-label="Card front">
    <h1 class="front-name">Cruise a Trikeway Houston</h1>
  </section>

  <section class="card card-back" aria-label="Card back">
    <div class="brand-block">
      <p class="brand-name">Cruise a Trikeway Houston</p>
      <p class="brand-tagline">Rentals available hourly or daily<br>(Book online)</p>
    </div>
    <div class="divider"></div>
    <div class="contact-block">
      <p class="person-name">Daniel Brooks</p>
      <p class="person-role">Founder</p>
      <p class="contact-line"><span class="contact-label">Phone:</span> (832) 555-0193</p>
      <p class="contact-line">www.cruiseatrikewayhouston.com</p>
    </div>
  </section>
</main>
</body>
</html>
```